Educational clinic needs a new webpage design

I have a relatively new website but I am unhappy with the design. I was hoping the look of it would more match my logo, brochures, business cards, and postcards. The content is good and it's already mobile ready. The designer used square space, which I would like to keep if possible. My website is www.harborlightstudyhouse.example

Target Market(s)

Parents of school age children

Industry/Entity Type

Education

Number of Pages Required

5+ page

Requirements
Must have
• Pictures must depict the diversity of our students. We service all ages, from preschool through college and our students come from varying races.
Should not have
• I try to avoid the word "tutoring" because what we do is so much more. I like the tag line of "results that go beyond traditional tutoring"

```html
<!DOCTYPE html>
<html lang="en">
<head>
<meta charset="utf-8">
<title>Harbor Light Study House — Home</title>
<link rel="stylesheet" href="https://fonts.googleapis.com/css2?family=EB+Garamond:wght@400;600&family=Roboto:wght@300;400&display=swap">
<style>
  :root {
    --black: #000000;
    --white: #ffffff;
    --brand: #6e3a98;
    --leaf: #7fb341;
    --ink: #1d1d1d;
    --nav: #d8d8d8;
    --hero-deep: #2e2536;
    --hero-mid: #5a4a63;
    --hero-warm: #8a6a52;
    --photo-warm: #b08a5c;
    --photo-skin: #7a5238;
    --photo-grey: #8b8f92;
    --photo-blue: #9fb8c8;
  }
  * { margin: 0; padding: 0; box-sizing: border-box; }
  html, body { width: 1200px; height: 2582px; overflow: hidden; background: var(--white); }
  body { position: relative; font-family: "Roboto", Arial, sans-serif; color: var(--ink); }

  .site-header { position: absolute; left: 0; top: 0; width: 1200px; height: 117px; background: var(--black); }
  .brand { position: absolute; left: 32px; top: 38px; display: flex; align-items: center; gap: 14px;
    font-weight: 400; font-size: 26px; color: var(--brand); letter-spacing: 0.5px; white-space: nowrap; }
  .brand-dot { width: 30px; height: 30px; border-radius: 50%; background: var(--brand); }
  .main-nav { position: absolute; top: 46px; left: 0; font-size: 23px; font-weight: 300; color: var(--nav); }
  .main-nav a { position: absolute; white-space: nowrap; color: inherit; text-decoration: none; }
  .main-nav a.is-current { color: var(--white); font-weight: 400; }

  .hero { position: absolute; left: 0; top: 117px; width: 1200px; height: 734px; overflow: hidden; }
  .hero-photo { position: absolute; inset: 0;
    background: linear-gradient(120deg, var(--hero-warm) 0%, var(--hero-mid) 35%, var(--hero-deep) 60%, #4d3f56 85%, var(--hero-warm) 100%); }
  .hero-shade { position: absolute; inset: 0; background: rgba(0,0,0,0.3); }
  .hero-title { position: absolute; left: 100px; width: 1000px; top: 218px; text-align: center;
    font-family: "EB Garamond", Georgia, serif; font-weight: 600; font-size: 46px; line-height: 61px; color: var(--white); }
  .hero-text { position: absolute; left: 100px; width: 1000px; top: 392px; text-align: center;
    font-family: "EB Garamond", Georgia, serif; font-weight: 400; font-size: 30px; line-height: 43px; color: var(--white); }

  .section-title { position: absolute; left: 0; width: 1200px; text-align: center;
    font-weight: 300; font-size: 50px; color: var(--brand); letter-spacing: 0.5px; }
  .photo { position: absolute; }
  .photo-reading { left: 132px; top: 1072px; width: 498px; height: 424px;
    background: linear-gradient(135deg, #ece9e4 0%, var(--photo-grey) 30%, var(--photo-skin) 55%, var(--photo-warm) 80%, #8a6a44 100%); }
  .photo-laptop { left: 568px; top: 1715px; width: 500px; height: 423px;
    background: linear-gradient(120deg, #4a4d50 0%, var(--photo-skin) 35%, var(--photo-grey) 60%, var(--photo-blue) 100%); }
  .body-copy { position: absolute; font-weight: 300; font-size: 33px; line-height: 44px; color: var(--ink); }
  .learn-more { position: absolute; display: flex; align-items: center; gap: 20px;
    font-weight: 300; font-size: 34px; color: var(--brand); text-decoration: none; white-space: nowrap; }
  .learn-more svg { color: var(--leaf); }

  .site-footer { position: absolute; left: 0; top: 2226px; width: 1200px; height: 356px; background: var(--black); color: var(--white); }
  .footer-contact { position: absolute; left: 130px; top: 84px; font-size: 20px; line-height: 28px; text-transform: uppercase; font-style: normal; }
  .footer-contact .gap { height: 27px; }
  .subscribe-label { position: absolute; left: 611px; top: 84px; font-size: 20px; text-transform: uppercase; }
  .subscribe-field { position: absolute; left: 612px; top: 124px; width: 412px; height: 62px;
    border: 3px solid var(--white); border-radius: 7px; }
  .subscribe-field svg { position: absolute; right: 14px; top: 13px; }
  .social-link { position: absolute; left: 612px; top: 2437px; width: 47px; height: 61px;
    border: 2px solid var(--white); border-radius: 8px; }
</style>
</head>
<body>
  <header class="site-header">
    <div class="brand"><span class="brand-dot"></span>Harbor Light Study House</div>
    <nav class="main-nav">
      <a class="is-current" style="left:474px">HOME</a>
      <a style="left:575px">SERVICES</a>
      <a style="left:717px">ABOUT US</a>
      <a style="left:863px">PAYMENTS</a>
      <a style="left:1013px">CONTACT US</a>
    </nav>
  </header>

  <section class="hero">
    <div class="hero-photo" role="img" aria-label="A diverse group of students of different races and ages, from preschool to college, learning together around classroom tables"></div>
    <div class="hero-shade"></div>
    <h1 class="hero-title">We offer learning programs for students of all ages<br>and learning types.</h1>
    <p class="hero-text">We strive to determine the needs of every child who walks through our doors<br>and find a way to address those needs. We are solution oriented and we get<br>results.</p>
  </section>

  <h2 class="section-title" style="top:928px">ABOUT</h2>
  <div class="photo photo-reading" role="img" aria-label="A young Black student reading a book in a lounge chair"></div>
  <p class="body-copy" style="left:689px;top:1064px;width:400px">Find out about our services, our methods, and the results of over a decade of teaching.</p>
  <a class="learn-more" style="left:687px;top:1290px">Learn More
    <svg width="56" height="16" viewBox="0 0 56 16"><path d="M0 8H54M46 1l8 7-8 7" fill="none" stroke="currentColor" stroke-width="3"/></svg>
  </a>

  <h2 class="section-title" style="top:1576px">CONTACT US</h2>
  <p class="body-copy" style="left:128px;top:1707px;width:420px">Are you ready to get your student confident in class? We are here to help you today!</p>
  <a class="learn-more" style="left:128px;top:1933px">Learn More
    <svg width="56" height="16" viewBox="0 0 56 16"><path d="M0 8H54M46 1l8 7-8 7" fill="none" stroke="currentColor" stroke-width="3"/></svg>
  </a>
  <div class="photo photo-laptop" role="img" aria-label="A Latina college student studying at a table with a laptop and notebooks"></div>

  <footer class="site-footer">
    <address class="footer-contact">
      Harbor Light Study House<br>
      418 Lantern Way<br>
      Bayview<br>
      IL, 60000
      <div class="gap"></div>
      555-014-2290<br>
      info@harborlightstudyhouse.example
    </address>
    <div class="subscribe-label">Subscribe</div>
    <div class="subscribe-field">
      <svg width="44" height="30" viewBox="0 0 44 30"><path d="M2 15H40M28 3l12 12-12 12" fill="none" stroke="#fff" stroke-width="3"/></svg>
    </div>
  </footer>
  <div class="social-link" role="img" aria-label="Social media link"></div>
</body>
</html>
```